Looking for Landingpage / Website Designer

We are looking for a Web Designer / Developer for our upcoming Start Up Websites. The first project will be a simple responsive business website with a CTA- Button and an optional Newsletter Opt-In. We do aim for a modern online business approach, since we are a young company.

It is necessary to understand, that we need a conversion orientated design, not a wordpress blog with widgets and galleries.

We are currently discussing how it is going to happen and what preferences we need to focus on.

What we know is, that it should be more of a landing page with an option of adding 2 or 3 Navigation points.

We even thought about using services like pagemarlo.com or formvista.com to have an easier approach for future customizations and A/B testing.

We'd love to see how you fit the design/colors to the upcoming logo
(which is not the final version yet )

hope you can do something about that.

For the Structure.

1. Bracket

Slogan plus a preview text of what we are offering. On the right side a video placeholder plus CTA button.

2. Bracket

Illustrating 3 Benefits. On the right side - Opt in for Contact/Newsletter and CTA Button

3. Bracket

Picture with text just like you have it with the testimonial

You can orientate yourself towards to that landing page example as well:

http://cdn2.quentarix.net/hub/53/file-581676469-png/Blog-Related_Images/pagemarlo_landing_page.png?t=1416543075530

If our collaboration is going well, we would like to stay in touch for further projects.

Reason: There are 3 Design we do really like but, don't fit exactly our needs. 5 Days max.

Reason: For final adjustments.

I just uploaded the final logo :) Thank you for your commitment so far!

Target Market(s)

Our targeted audience could be almost everybody, who looks for an average paid side job (students, unemployed, house wives and whatever you can imagine). Maybe this is enough information for you to get a mere perception of what this is all about.

Industry/Entity Type

Business

Coding

Coded - Design and coding required

Font styles to use
Serif
Sans Serif

Colors
acd037
5c5c5c
33a6d7

Requirements
Must have
• Registration Opt-In
Responsive on any Device
Customizable
A benefits navigation just like in that example I've uploaded.
Nice to have
• As fast as possible ;D

```html
<!DOCTYPE html>
<html lang="en">
<head>
<meta charset="utf-8">
<title>Workvana – Finding a job now is easier than ever</title>
<link href="https://fonts.googleapis.com/css2?family=Raleway:wght@400;500;600;700;800&display=swap" rel="stylesheet">
<style>
:root{
  --ink:#1e1e1e;
  --text:#333333;
  --muted:#5c5c5c;
  --soft:#8a8a8a;
  --green:#4a9a3c;
  --green-dark:#2f6a26;
  --green-deep:#1f4a19;
  --hero-a:#3c8d33;
  --hero-b:#55ab45;
  --panel:#ececec;
  --panel-border:#d6d6d6;
  --white:#ffffff;
  --field-border:#dcdcdc;
}
*{box-sizing:border-box;margin:0;padding:0}
html,body{width:720px;height:1200px;overflow:hidden}
body{font-family:"Raleway",Arial,sans-serif;color:var(--text);background:var(--white);position:relative}
.abs{position:absolute}

/* top bar */
.topbar{left:0;top:0;width:720px;height:42px;background:var(--ink)}
.brand-box{left:78px;top:0;width:180px;height:54px;background:var(--white);display:flex;align-items:center;justify-content:center;gap:7px;z-index:2;box-shadow:0 2px 4px rgba(0,0,0,.15)}
.brand-dot{width:22px;height:22px;border-radius:50%;background:var(--green)}
.brand-name{font-size:21px;font-weight:700;color:var(--green);letter-spacing:-.3px}
.social{right:78px;top:11px;display:flex;gap:6px}
.social span{width:19px;height:19px;border-radius:50%;background:#5a5a5a;display:block}

/* hero */
.hero{left:0;top:42px;width:720px;height:348px;background:linear-gradient(160deg,var(--hero-a) 0%,#459c3a 50%,var(--hero-b) 100%)}
.hero-title{left:78px;top:101px;width:300px;font-size:26px;line-height:30px;font-weight:600;color:var(--white);text-transform:uppercase}
.hero-rule{left:78px;top:175px;width:65px;height:5px;background:var(--green-deep)}
.hero-copy{left:78px;top:192px;width:285px;font-size:12.2px;line-height:18.5px;color:var(--white)}
.cta{left:78px;top:288px;width:180px;height:36px;background:var(--white);border-radius:2px;color:var(--green-deep);font-size:11px;font-weight:700;display:flex;align-items:center;justify-content:center;text-transform:uppercase}
.video{left:390px;top:108px;width:252px;height:156px;background:#202020}

/* offer */
.offer-title{left:78px;top:436px;font-size:21px;font-weight:700;color:var(--text);text-transform:uppercase}
.offer-sub{left:79px;top:462px;font-size:11.5px;color:var(--soft)}
.feature{left:78px;width:280px}
.feature svg{position:absolute;left:2px;top:0;width:30px;height:30px}
.feature h3{position:absolute;left:52px;top:-4px;font-size:15px;font-weight:600;color:var(--text);white-space:nowrap}
.feature p{position:absolute;left:52px;top:16px;width:225px;font-size:8.4px;line-height:14.6px;color:var(--muted)}

.contact{left:390px;top:438px;width:252px;height:324px;background:var(--panel);border:3px solid var(--panel-border)}
.contact h2{position:absolute;left:14px;top:19px;font-size:14.5px;font-weight:600;color:var(--text)}
.contact .sub{position:absolute;left:14px;top:42px;font-size:11.3px;color:var(--soft)}
.field{position:absolute;left:14px;width:216px;height:30px;background:var(--white);border:1px solid var(--field-border);font-size:8.5px;color:var(--soft);padding-left:12px;display:flex;align-items:center}
.submit{position:absolute;left:15px;top:243px;width:216px;height:36px;background:var(--green);color:var(--white);font-size:8.5px;font-weight:700;text-transform:uppercase;display:flex;align-items:center;justify-content:center;border-radius:2px}

/* stories */
.stories{left:0;top:810px;width:720px;height:300px;background:var(--panel)}
.stories-title{left:0;top:849px;width:720px;text-align:center;font-size:21px;font-weight:700;color:var(--text);text-transform:uppercase}
.stories-sub{left:0;top:876px;width:720px;text-align:center;font-size:11.5px;color:var(--soft)}
.story{top:929px;width:180px;height:126px}
.avatar{position:absolute;left:0;top:0;width:36px;height:36px;border:3px solid var(--white);background:linear-gradient(160deg,#c9a48c,#8a6a58)}
.story .name{position:absolute;left:48px;top:8px;font-size:11.5px;font-weight:600;color:var(--text)}
.story .role{position:absolute;left:48px;top:22px;font-size:8.5px;color:var(--soft)}
.quote{position:absolute;left:0;top:48px;width:180px;height:78px;background:var(--white);padding:10px 4px 0 4px;font-size:8.4px;line-height:14.5px;color:var(--muted)}
.quote::before{content:"";position:absolute;left:12px;top:-7px;border-left:7px solid transparent;border-right:7px solid transparent;border-bottom:7px solid var(--white)}

/* footer */
.footer{left:0;top:1110px;width:720px;height:90px;background:var(--ink)}
.footer-copy{left:77px;top:1136px;font-size:8.5px;line-height:15px;color:#8a8a8a}
.footer-brand{left:545px;top:1140px;display:flex;align-items:center;gap:5px}
.footer-brand .brand-dot{width:19px;height:19px}
.footer-brand .brand-name{font-size:17px}
</style>
</head>
<body>

<header>
  <div class="abs topbar"></div>
  <div class="abs brand-box"><span class="brand-dot"></span><span class="brand-name">Workvana</span></div>
  <nav class="abs social" aria-label="Social links"><span></span><span></span><span></span></nav>
</header>

<section aria-label="Introduction">
  <div class="abs hero" role="img" aria-label="Green low-poly background"></div>
  <h1 class="abs hero-title">Finding a job now is easier than ever</h1>
  <div class="abs hero-rule"></div>
  <p class="abs hero-copy">Nam liber tempor cum soluta nobis eleifend option congue nihil imperdiet doming id quod mazim placerat facer possim assum. Lorem ipsum dolor sit amet, con-sectetuer adipiscing elit, sed diam nonummy.</p>
  <a class="abs cta">Call to action</a>
  <div class="abs video" role="img" aria-label="Video placeholder"></div>
</section>

<section aria-label="What do we offer">
  <h2 class="abs offer-title">What do we offer</h2>
  <p class="abs offer-sub">A descriptive sub title that explains what comes below.</p>

  <div class="abs feature" style="top:512px">
    <svg viewBox="0 0 30 30"><path d="M29 2 L1 13 L9 16 L11 27 L16 19 L23 25 Z" fill="#4a9a3c"/><path d="M9 16 L29 2 L11 20 Z" fill="#2f6a26"/></svg>
    <h3>First feature title</h3>
    <p>Consetetur sadipscing elitr, sed diam nonumy eirmod teminvidunt ut labore et dolore magna aliquyam erator invidunt ut labore.</p>
  </div>

  <div class="abs feature" style="top:603px">
    <svg viewBox="0 0 30 30"><path d="M4 24 C3 12 12 4 28 5 C28 18 20 26 8 23 Z" fill="#4a9a3c"/><path d="M2 28 L20 12" stroke="#fff" stroke-width="2" fill="none"/></svg>
    <h3>Second feature title</h3>
    <p>Consetetur sadipscing elitr, sed diam nonumy eirmod teminvidunt ut labore et dolore magna aliquyam erator invidunt ut labore.</p>
  </div>

  <div class="abs feature" style="top:694px">
    <svg viewBox="0 0 30 30"><path d="M26 4 C18 4 12 9 9 16 L14 21 C21 18 26 12 26 4 Z" fill="#4a9a3c"/><path d="M9 16 L4 15 L9 10 L13 11 Z M14 21 L15 26 L20 21 L19 17 Z" fill="#4a9a3c"/><path d="M8 19 L4 26 L11 22 Z" fill="#4a9a3c"/></svg>
    <h3>Third feature title</h3>
    <p>Consetetur sadipscing elitr, sed diam nonumy eirmod teminvidunt ut labore et dolore magna aliquyam erator invidunt ut labore.</p>
  </div>

  <form class="abs contact" aria-label="Contact form">
    <h2>Contact Us</h2>
    <p class="sub">Fill and submit the form to contact us</p>
    <div class="field" style="top:75px">First name</div>
    <div class="field" style="top:117px">Last name</div>
    <div class="field" style="top:159px">Email</div>
    <div class="field" style="top:201px">Phone number</div>
    <div class="submit">Submit form</div>
  </form>
</section>

<section aria-label="Success stories">
  <div class="abs stories"></div>
  <h2 class="abs stories-title">Success stories</h2>
  <p class="abs stories-sub">Short testimonials from successful members</p>

  <article class="abs story" style="left:78px">
    <div class="avatar" role="img" aria-label="Portrait of Marion Hale"></div>
    <div class="name">Marion Hale</div>
    <div class="role">Business person</div>
    <p class="quote">Nam liber tempor cum soluta nobis eleifend option congue nihil imperdiet doming id quod mazim placerat facer possim assum.</p>
  </article>

  <article class="abs story" style="left:270px">
    <div class="avatar" role="img" aria-label="Portrait of Devin Park"></div>
    <div class="name">Devin Park</div>
    <div class="role">Business person</div>
    <p class="quote">Nam liber tempor cum soluta nobis eleifend option congue nihil imperdiet doming id quod mazim placerat facer possim assum.</p>
  </article>

  <article class="abs story" style="left:462px">
    <div class="avatar" role="img" aria-label="Portrait of Nora Ellis"></div>
    <div class="name">Nora Ellis</div>
    <div class="role">Business person</div>
    <p class="quote">Nam liber tempor cum soluta nobis eleifend option congue nihil imperdiet doming id quod mazim placerat facer possim assum.</p>
  </article>
</section>

<footer>
  <div class="abs footer"></div>
  <p class="abs footer-copy">Duis autem vel eum iriure dolor in hendrerit in vulputate<br>Avelit esse molestie consequat, vel illum</p>
  <div class="abs footer-brand"><span class="brand-dot"></span><span class="brand-name">Workvana</span></div>
</footer>

</body>
</html>
```